New Card

Photography business
I want a sleek simple card that screams rich and classy. Black/Gold or silver font. No photos or images but would love a new logo When I hand someone my card I want compliments
Updates
My fiancé reminded me in 5 short months my name will change so I have changed my name to Colleen Marwick
Also my BRAND is Lantern Bloom Photography, not my name. Thanks
Industry/Entity Type
Business
Contact Information for Business Card
Lantern Bloom Photography
Colleen Marwick-owner
482 W. Thornbury Rd.
Ashgrove Point, NJ 08000
(609)555-0142
colleen@lanternbloomstudio.example
Look and feel
Each slider illustrates characteristics of the customer's brand and the style your logo design should communicate.

```html
<!DOCTYPE html>
<html lang="en">
<head>
<meta charset="utf-8">
<title>Lantern Bloom Photography — Business Card</title>
<link href="https://fonts.googleapis.com/css2?family=Great+Vibes&family=Questrial&display=swap" rel="stylesheet">
<style>
  :root {
    --backdrop: #2a2420;
    --card-black: #0d0d0e;
    --card-sheen: #2b2b2e;
    --gold: #e9a93a;
    --silver: #eeeeee;
  }
  * { margin: 0; padding: 0; box-sizing: border-box; }
  html, body {
    width: 1200px; height: 855px; overflow: hidden;
    background: var(--backdrop);
  }
  .stage {
    position: relative; width: 1200px; height: 855px;
    display: flex; align-items: center; justify-content: center; gap: 50px;
  }
  .card {
    position: relative;
    width: 530px; height: 303px;
    border-radius: 26px;
    background: linear-gradient(135deg, var(--card-sheen) 0%, var(--card-black) 45%, var(--card-black) 100%);
    box-shadow: 0 18px 40px rgba(0,0,0,.55);
    overflow: hidden;
  }
  /* Front */
  .brand {
    position: absolute; left: 70px; top: 92px;
    display: flex; align-items: center; gap: 14px;
  }
  .brand-dot {
    width: 26px; height: 26px; border-radius: 50%;
    background: var(--gold);
  }
  .brand-name {
    font-family: "Great Vibes", cursive;
    font-size: 48px; line-height: 1; color: var(--gold);
  }
  .brand-tagline {
    position: absolute; left: 220px; top: 150px;
    font-family: "Questrial", sans-serif;
    font-size: 15px; letter-spacing: 7px; color: var(--silver);
  }
  .card-front .website {
    position: absolute; left: 120px; top: 212px;
    font-family: "Questrial", sans-serif;
    font-size: 16px; letter-spacing: .5px; color: var(--silver);
  }
  /* Back */
  .owner-name {
    position: absolute; left: 120px; top: 46px;
    font-family: "Great Vibes", cursive; font-weight: 400;
    font-size: 46px; line-height: 1; color: var(--gold);
  }
  .owner-role {
    position: absolute; left: 60px; top: 108px;
    font-family: "Questrial", sans-serif;
    font-size: 21px; color: var(--silver);
  }
  .contact-list {
    position: absolute; left: 40px; top: 160px;
    list-style: none;
    font-family: "Questrial", sans-serif;
    font-size: 15px; color: var(--silver);
  }
  .contact-list li {
    display: flex; align-items: center; gap: 10px;
    height: 26px;
  }
  .contact-icon { width: 16px; height: 16px; flex: none; }
  .contact-icon circle { fill: var(--gold); }
  .contact-icon path { fill: var(--card-black); }
  .contact-list .address,
  .contact-list .web { font-size: 17px; }
  .contact-list .web { padding-left: 26px; }
</style>
</head>
<body>
<main class="stage">
  <section class="card card-front" aria-label="Business card front">
    <div class="brand">
      <span class="brand-dot"></span>
      <span class="brand-name">Lantern Bloom</span>
    </div>
    <span class="brand-tagline">Photography</span>
    <p class="website">www.lanternbloomstudio.example</p>
  </section>

  <section class="card card-back" aria-label="Business card back">
    <h1 class="owner-name">Colleen Marwick</h1>
    <p class="owner-role">Owner/Photographer</p>
    <ul class="contact-list">
      <li>
        <svg class="contact-icon" viewBox="0 0 16 16" aria-hidden="true">
          <circle cx="8" cy="8" r="8"/>
          <path d="M5 4h2l1 2.2-1.2.8c.5 1 1.2 1.7 2.2 2.2l.8-1.2L12 9v2c0 .6-.4 1-1 1C7.1 12 4 8.9 4 5c0-.6.4-1 1-1z"/>
        </svg>
        <span>(609)555-0142</span>
      </li>
      <li>
        <svg class="contact-icon" viewBox="0 0 16 16" aria-hidden="true">
          <circle cx="8" cy="8" r="8"/>
          <path d="M4 5h8v6H4zM4.6 5.4 8 8.2l3.4-2.8v.9L8 9.1 4.6 6.3z"/>
        </svg>
        <span>colleen@lanternbloomstudio.example</span>
      </li>
      <li class="address">
        <svg class="contact-icon" viewBox="0 0 16 16" aria-hidden="true">
          <circle cx="8" cy="8" r="8"/>
          <path d="M8 3a3 3 0 0 1 3 3c0 2.2-3 6-3 6S5 8.2 5 6a3 3 0 0 1 3-3zm0 1.9a1.1 1.1 0 1 0 0 2.2 1.1 1.1 0 0 0 0-2.2z"/>
        </svg>
        <span>482 W. Thornbury Rd. Ashgrove Point, NJ 08000</span>
      </li>
      <li class="web">www.lanternbloomstudio.example</li>
    </ul>
  </section>
</main>
</body>
</html>
```